brightmolar flyer on both sides

Need to design a flyer for brightmolar practice
emphasis on quality patient care

incorporate our partners QMP, RTWA and VLOKE.
ALL other health funds accepted with TORVEX

special offer: bring your family in for no gap dental clean,exam,x ray and fluoride treatments

second page-cosmetic dentistry
MODEL- WITH NICE TEETH

Aesthetic assessment- no charge for consult only with printed treatment plan at the end of consult. 20% off makeovers

sample implant flyer we used previously attached

Target Market(s)

families and patients looking for cosmetic dentistry

Industry/Entity Type

Health

Requirements
Must have
• our practice logo, phone number,web address, address
Nice to have
• eye catching, less clinical

```html
<!DOCTYPE html>
<html lang="en">
<head>
<meta charset="utf-8">
<title>Bright Molar Flyer</title>
<link rel="stylesheet" href="https://fonts.googleapis.com/css2?family=Ubuntu:wght@400;500;700&display=swap">
<style>
:root{
  --bg:#e4e5e8;
  --paper:#ffffff;
  --cyan:#3bb3d9;
  --cyan-deep:#1f9ccb;
  --navy:#2a2f86;
  --purple:#6b63b5;
  --lilac:#a7a3d6;
  --lilac-soft:#d9d7ef;
  --ink:#2c2c34;
  --ink-soft:#555560;
  --brand:#2f6fb5;
  --royal:#2c6fd0;
}
*{margin:0;padding:0;box-sizing:border-box}
html,body{width:1200px;height:905px;overflow:hidden}
body{background:var(--bg);font-family:"Ubuntu",Arial,sans-serif;position:relative;color:var(--ink)}
.flyer{position:absolute;background:var(--paper);overflow:hidden;box-shadow:0 2px 8px rgba(0,0,0,.25)}
.flyer--family{left:134px;top:162px;width:470px;height:664px}
.flyer--cosmetic{left:644px;top:77px;width:468px;height:663px}
.flyer__art{position:absolute;inset:0;width:100%;height:100%}
.abs{position:absolute}

.brand{position:absolute;text-align:center;color:var(--brand)}
.brand__mark{width:30px;height:30px;border-radius:50%;border:3px solid var(--cyan);margin:0 auto 6px}
.brand__name{font-weight:700;font-size:11px;letter-spacing:.2px}
.brand__tag{font-size:8px;color:var(--ink);margin-top:1px}

.photo{position:absolute}
.photo--family{left:11px;top:158px;width:390px;height:282px;
  background:linear-gradient(180deg,#dcd8d6 0%,#c9b7aa 45%,#b9b3b0 100%);
  clip-path:path("M0,0 L189,0 C289,7 349,42 374,112 C394,172 374,242 329,282 L0,282 Z")}
.photo--model{left:140px;top:0;width:290px;height:345px;
  background:radial-gradient(ellipse at 50% 45%,#f1d6c5 0%,#e8c9b3 40%,#eef0f3 80%)}

.promo-tag{left:16px;top:386px;width:196px;height:52px;background:var(--paper);padding:4px 0 0 12px}
.promo-tag__title{font-size:20px;font-weight:700;color:var(--ink);letter-spacing:.2px}
.promo-tag__title span{color:var(--cyan)}
.promo-tag__sub{font-size:13px;color:var(--ink-soft);margin-top:1px}

.offer-band{left:0;top:441px;width:296px;height:88px;background:var(--cyan);color:#fff;font-weight:500}
.offer-band__gap{position:absolute;left:28px;top:34px;font-size:16px}
.offer-band__list{position:absolute;left:98px;top:10px;font-size:13px;line-height:25px;list-style:none}
.offer-band__list li::before{content:"▪ ";font-size:10px}

.providers__head{left:296px;top:476px;width:130px;text-align:center;font-size:11px;font-weight:500;color:var(--ink-soft);line-height:15px}
.fund{position:absolute;font-weight:700;display:flex;align-items:center;gap:4px}
.fund__dot{width:12px;height:12px;border-radius:50%}
.fund--rtwa{left:276px;top:526px;font-size:20px;color:var(--royal)}
.fund--qmp{left:362px;top:531px;font-size:20px;color:#d0263f}
.fund--vloke{left:276px;top:580px;font-size:19px;color:#169fd9}
.fund--kinfolk{left:400px;top:578px;font-size:9px;color:#d0287f;width:56px;text-align:center;line-height:10px}

.health-note{left:0;top:552px;width:260px;text-align:center;font-size:10.5px;color:var(--cyan-deep);font-weight:500}
.claims{left:0;top:578px;width:260px;text-align:center}
.claims__name{font-size:17px;font-weight:700;color:var(--ink);display:inline-flex;align-items:center;gap:6px}
.claims__name i{display:inline-block;width:12px;height:12px;border-radius:50%;background:#e3c21a}
.claims__tag{font-size:9.5px;color:var(--ink);margin-top:4px}

.assess-bar{left:0;top:347px;width:400px;height:34px;background:var(--paper);
  clip-path:polygon(0 0,100% 0,94% 100%,0 100%);font-size:19px;font-weight:500;padding:6px 0 0 170px;color:var(--ink)}
.assess-bar span{color:var(--cyan)}
.consult-note{left:254px;top:406px;color:#fff;font-size:13px;font-weight:500;line-height:17px}
.discount{left:48px;top:418px;width:154px;height:154px;background:var(--navy);padding:6px}
.discount__inner{width:100%;height:100%;background:var(--paper);text-align:center;padding-top:26px}
.discount__big{font-size:52px;font-weight:700;color:var(--cyan);display:inline-flex;align-items:center;line-height:1}
.discount__pct{display:inline-flex;flex-direction:column;font-size:22px;line-height:.9;color:var(--cyan)}
.discount__pct small{font-size:18px;color:var(--ink)}
.discount__label{font-size:19px;font-weight:500;color:var(--ink);margin-top:4px}
</style>
</head>
<body>

<section class="flyer flyer--family">
  <svg class="flyer__art" viewBox="0 0 470 664" aria-hidden="true">
    <polygon points="290,0 470,0 470,170" fill="var(--lilac-soft)"/>
    <polygon points="330,0 470,0 470,120 400,60" fill="var(--lilac)" opacity=".7"/>
    <polygon points="380,60 470,150 470,330 330,200" fill="var(--purple)" opacity=".55"/>
    <polygon points="230,150 330,110 440,200 360,230" fill="var(--lilac)" opacity=".6"/>
    <polygon points="400,170 470,120 470,260" fill="var(--navy)" opacity=".5"/>
    <path d="M0,68 Q130,170 340,158 Q140,188 0,76 Z" fill="var(--cyan)"/>
    <path d="M200,155 C350,140 470,220 445,330 C430,390 390,425 340,440 C385,400 405,330 385,270 C360,200 300,165 200,158 Z" fill="var(--navy)"/>
    <path d="M330,441 C400,420 450,390 470,360 L470,441 Z" fill="var(--cyan)" opacity=".9"/>
    <path d="M470,392 C330,450 240,550 218,664 L246,664 C262,560 340,470 470,418 Z" fill="var(--purple)" opacity=".75"/>
    <path d="M470,425 C350,480 270,570 258,664 L268,664 C282,575 360,490 470,437 Z" fill="var(--lilac)"/>
  </svg>

  <div class="brand" style="left:196px;top:32px;width:90px">
    <div class="brand__mark"></div>
    <div class="brand__name">BRIGHT MOLAR</div>
    <div class="brand__tag">Putting patients first</div>
  </div>

  <div class="photo photo--family" role="img" aria-label="Photo of a smiling family of four: father, two children and mother"></div>

  <div class="abs promo-tag">
    <div class="promo-tag__title">SPECIAL<span>PROMO</span></div>
    <div class="promo-tag__sub">bring your family in for :</div>
  </div>

  <div class="abs offer-band">
    <div class="offer-band__gap">NO GAP</div>
    <ul class="offer-band__list">
      <li>Dental Clean</li>
      <li>Exam &nbsp;▪ X Ray</li>
      <li>Fluoride Treatments</li>
    </ul>
  </div>

  <div class="abs providers__head">We are preferred<br>providers for:</div>
  <div class="fund fund--rtwa"><span class="fund__dot" style="background:var(--royal)"></span>RTWA</div>
  <div class="fund fund--qmp"><span class="fund__dot" style="background:#d0263f"></span>QMP</div>
  <div class="fund fund--vloke">VLOKE</div>
  <div class="fund fund--kinfolk">KINFOLK MUTUAL</div>

  <div class="abs health-note">this offer applies to all health funds</div>
  <div class="abs claims">
    <div class="claims__name"><i></i>TORVEX</div>
    <div class="claims__tag">Fast claims... on the spot</div>
  </div>
</section>

<section class="flyer flyer--cosmetic">
  <svg class="flyer__art" viewBox="0 0 468 663" aria-hidden="true">
    <defs>
      <linearGradient id="deep-blue" x1="0" y1="0" x2="1" y2="1">
        <stop offset="0" stop-color="#2f7fd8"/>
        <stop offset="1" stop-color="#2a3fa8"/>
      </linearGradient>
    </defs>
    <rect width="468" height="380" fill="#eef0f7"/>
    <polygon points="0,0 190,0 0,200" fill="var(--lilac)" opacity=".8"/>
    <polygon points="0,120 150,260 0,380" fill="var(--purple)" opacity=".55"/>
    <polygon points="60,0 200,0 120,120" fill="var(--lilac-soft)"/>
    <polygon points="0,260 200,380 0,380" fill="var(--lilac)" opacity=".7"/>
    <rect y="375" width="468" height="288" fill="url(#deep-blue)"/>
    <polygon points="0,375 200,375 0,560" fill="#4a8fe0" opacity=".7"/>
    <polygon points="120,500 320,663 0,663" fill="#5aa7ea" opacity=".55"/>
    <polygon points="300,520 468,440 468,663 360,663" fill="#8ec6ef" opacity=".45"/>
    <polygon points="200,600 300,663 120,663" fill="var(--navy)" opacity=".6"/>
    <polygon points="380,375 468,375 468,470" fill="var(--purple)" opacity=".6"/>
    <path d="M170,380 L468,380 L468,520 C468,560 430,565 400,565 L300,565 C240,565 210,520 170,380 Z" fill="var(--cyan)"/>
  </svg>

  <div class="photo photo--model" role="img" aria-label="Photo of a smiling blonde woman resting her face on her hands"></div>

  <div class="brand" style="left:350px;top:40px;width:90px">
    <div class="brand__mark"></div>
    <div class="brand__name">BRIGHT MOLAR</div>
    <div class="brand__tag">Putting patients first</div>
  </div>

  <div class="abs assess-bar">Aesthetic <span>Assessment</span></div>

  <div class="abs consult-note">No Charge for consult.<br>Printed treatment plan<br>at the end of consult</div>

  <div class="abs discount">
    <div class="discount__inner">
      <div class="discount__big">20<span class="discount__pct">%<small>off</small></span></div>
      <div class="discount__label">makeovers</div>
    </div>
  </div>
</section>

</body>
</html>
```